Certified Legal Nurse Consultant business needs a postcard design

Need a postcard that advertises to target market of attorneys. I am a registered nurse who helps lawyers with the medical issues on their cases. I want this card to highlight the benefit of my services versus the competition. Please see attached document for more info.
Updates

Reason: Many of the 20 designs I received were from the same designer, but just altered slightly. I was expecting ~20 original/unique designs. Thanks!

Target Market(s)

attorneys (lawyers)

Industry/Entity Type

Business

Font styles to use
Serif

Colors
3176b5
0355a3

Requirements
Must have
• my photo, business name and address, phone number, web address, description of how my business is better than the competition (see PDF file sent)

```html
<!DOCTYPE html>
<html lang="en">
<head>
<meta charset="utf-8">
<title>R. Halvorsen &amp; Associates – Postcard</title>
<link href="https://fonts.googleapis.com/css2?family=Crimson+Pro:ital,wght@0,300;0,400;0,500;1,400&family=Raleway:wght@400;500;600;700&display=swap" rel="stylesheet">
<style>
  :root{
    --blue:#5b7bb5;
    --blue-deep:#4a68a3;
    --frame:#e2ddd2;
    --line:#d9dce4;
    --column:#f1f2f6;
    --lavender:#e7eaf5;
    --circle:#b9c1df;
    --accent:#f4a11d;
    --ink:#1f1f1f;
    --edge:#b7c2d9;
    --white:#ffffff;
    --serif:"Crimson Pro", Georgia, serif;
    --sans:"Raleway", Arial, sans-serif;
  }
  *{box-sizing:border-box;margin:0;padding:0}
  html,body{width:1200px;height:944px;overflow:hidden;background:var(--white)}
  .canvas{position:relative;width:1200px;height:944px}
  .card{position:absolute;top:0;width:472px;height:944px;background:var(--white);border:1px solid var(--edge);overflow:hidden}
  .card--front{left:2px}
  .card--back{left:721px}
  .card__band{position:absolute;left:0;right:0;height:9px;background:var(--blue)}
  .card__band::after{content:"";position:absolute;left:0;right:0;height:3px;background:var(--lavender)}
  .card__band--top{top:0}
  .card__band--top::after{bottom:-3px}
  .card__band--bottom{bottom:0}
  .card__band--bottom::after{top:-3px}
  .rules{position:absolute;left:0;width:100%}
  .titlebox{position:absolute;border:6px solid var(--frame);padding:3px;background:var(--white)}
  .titlebox__inner{width:100%;height:100%;background:var(--blue);color:var(--white);display:flex;align-items:center;justify-content:center;text-align:center}
  .brand{font-family:var(--sans);font-weight:600;font-size:19px;letter-spacing:.3px}
  .column-area{position:absolute;top:120px;width:36px;height:814px;background:var(--column)}
  .column-area--left{left:9px}
  .column-area--right{right:9px}
  .portrait{position:absolute;left:87px;top:130px;width:300px;height:398px;border:4px solid var(--accent);background:linear-gradient(160deg,#3a3836 0%,#1c1b1b 60%,#2a2624 100%)}
  .caption{position:absolute;left:0;width:100%;top:538px;text-align:center;font-family:var(--sans);font-size:10.5px;color:var(--ink)}
  .headline{font-family:var(--serif);font-size:29px;line-height:34px;font-weight:400}
  .welcome{position:absolute;left:0;width:100%;top:654px;text-align:center;font-family:var(--serif);font-style:italic;font-size:14px;color:var(--ink)}
  .swoosh{position:absolute;left:118px;width:236px;height:6px}
  .services{position:absolute;left:30px;width:412px;top:690px;text-align:center;font-family:var(--serif);font-weight:300;font-size:17.5px;line-height:20px;color:var(--ink);white-space:nowrap}
  .guarantee{position:absolute;left:0;width:100%;top:802px;text-align:center;font-family:var(--sans);font-weight:700;font-size:22px;color:var(--blue)}
  .contact{position:absolute;top:858px;font-family:var(--sans);font-size:13.5px;line-height:17px;color:var(--ink);font-style:normal}
  .contact--web{left:29px}
  .contact--post{left:248px}
  .contact__name{color:var(--blue)}
  .section-tag{position:absolute;border:2px solid var(--frame);padding:2px;background:var(--white)}
  .section-tag__inner{height:100%;background:var(--lavender);border:1.5px solid var(--blue);display:flex;align-items:center;justify-content:center;font-family:var(--serif);font-weight:400;font-size:24px;color:var(--blue-deep);letter-spacing:.3px}
  .about{position:absolute;left:25px;top:156px;width:418px;height:206px;border:6px solid var(--frame);padding:3px;background:var(--white)}
  .about__text{height:100%;background:var(--blue);color:var(--white);font-family:var(--sans);font-size:12.8px;line-height:17px;letter-spacing:.15px;text-align:justify;text-align-last:center;padding:14px 14px 0}
  .benefit{position:absolute;left:0;width:100%;height:112px}
  .benefit__dot{position:absolute;left:44px;top:25px;width:72px;height:72px;border-radius:50%;background:var(--circle);border:4px solid var(--frame)}
  .benefit__box{position:absolute;left:149px;top:0;width:280px;height:112px;background:var(--blue);color:var(--white);padding:4px 8px 0 8px}
  .benefit__box::before{content:"";position:absolute;left:-25px;top:40px;border-style:solid;border-width:16px 25px 16px 0;border-color:transparent var(--blue) transparent transparent}
  .benefit__title{display:flex;align-items:center;gap:6px;font-family:var(--serif);font-variant:small-caps;font-weight:400;font-size:16px;line-height:18px;color:var(--white)}
  .benefit__title::after{content:"";flex:1;height:1px;background:var(--lavender)}
  .benefit__body{font-family:var(--sans);font-size:15px;line-height:19px;margin-top:2px}
  .benefit__body--small{font-size:13.3px;line-height:17px;margin-top:0}
</style>
</head>
<body>
<div class="canvas">

  <!-- Front -->
  <section class="card card--front">
    <div class="card__band card__band--top"></div>
    <svg class="rules" style="top:48px;height:50px" viewBox="0 0 472 50" aria-hidden="true">
      <g stroke="var(--line)" stroke-width="1">
        <line x1="0" y1="6" x2="52" y2="6"/><line x1="0" y1="20" x2="52" y2="20"/><line x1="0" y1="34" x2="52" y2="34"/>
        <line x1="420" y1="6" x2="472" y2="6"/><line x1="420" y1="20" x2="472" y2="20"/><line x1="420" y1="34" x2="472" y2="34"/>
      </g>
    </svg>
    <div class="column-area column-area--left" role="img" aria-label="Decorative classical column along the left edge"></div>
    <div class="column-area column-area--right" role="img" aria-label="Decorative classical column along the right edge"></div>

    <div class="titlebox" style="left:51px;top:33px;width:370px;height:71px">
      <div class="titlebox__inner"><span class="brand">R. HALVORSEN &amp; ASSOCIATES, LLC</span></div>
    </div>

    <div class="portrait" role="img" aria-label="Portrait photo of the nurse consultant in a dark blazer"></div>
    <p class="caption">Claire M. Halvorsen RN, BSN, MPA, CCM, CLNC</p>

    <div class="titlebox" style="left:51px;top:559px;width:372px;height:87px">
      <div class="titlebox__inner"><h1 class="headline">Certified Legal Nurse<br>Consultants</h1></div>
    </div>

    <svg class="swoosh" style="top:651px" viewBox="0 0 236 6" preserveAspectRatio="none" aria-hidden="true"><path d="M0 5 Q118 -2 236 5" fill="none" stroke="var(--blue)" stroke-width="1.5"/></svg>
    <p class="welcome">Welcome to Healthcare Expertise</p>
    <svg class="swoosh" style="top:673px" viewBox="0 0 236 6" preserveAspectRatio="none" aria-hidden="true"><path d="M0 1 Q118 8 236 1" fill="none" stroke="var(--blue)" stroke-width="1.5"/></svg>

    <p class="services">Screen Cases For Merit | Develop Medical<br>Summaries | Research Authoritative Literature |<br>Locate Testifying Experts | Identify Adherences To<br>And Deviations From Standard Of Care</p>

    <p class="guarantee">100% Risk-Free Guarantee!</p>

    <address class="contact contact--web">www.halvorsen-partners.com<br>claire@halvorsen-partners.com<br>(612) 555-0187</address>
    <address class="contact contact--post"><span class="contact__name">R. Halvorsen &amp; Associates LLC</span><br>2190 Larkspur Lane<br>Cedar Ridge, MN 55310</address>
    <div class="card__band card__band--bottom"></div>
  </section>

  <!-- Back -->
  <section class="card card--back">
    <div class="card__band card__band--top"></div>
    <svg class="rules" style="top:44px;height:50px" viewBox="0 0 472 50" aria-hidden="true">
      <g stroke="var(--line)" stroke-width="1">
        <line x1="0" y1="6" x2="52" y2="6"/><line x1="0" y1="20" x2="52" y2="20"/><line x1="0" y1="34" x2="52" y2="34"/>
        <line x1="420" y1="6" x2="472" y2="6"/><line x1="420" y1="20" x2="472" y2="20"/><line x1="420" y1="34" x2="472" y2="34"/>
      </g>
    </svg>
    <div class="titlebox" style="left:50px;top:33px;width:370px;height:65px">
      <div class="titlebox__inner"><span class="brand">R. HALVORSEN &amp; ASSOCIATES, LLC</span></div>
    </div>

    <svg class="rules" style="top:118px;height:36px" viewBox="0 0 472 36" aria-hidden="true">
      <g stroke="var(--line)" stroke-width="1"><line x1="30" y1="10" x2="440" y2="10"/><line x1="30" y1="26" x2="440" y2="26"/></g>
    </svg>
    <div class="section-tag" style="left:131px;top:117px;width:206px;height:36px">
      <h2 class="section-tag__inner">WHO WE ARE:</h2>
    </div>

    <div class="about">
      <p class="about__text">Claire M. Halvorsen is a Certified Legal Nurse Consultant who has actively worked as a Registered Nurse for over 26 years. Areas of expertise include virtually every healthcare setting, including hospital, home care, nursing home, case management, clinical research, and outpatient care. During this time, she has reviewed, critiqued, and summarized thousands of medical records. As President and CEO, Claire leads a team of Certified Legal Nurse Consultants to best serve the needs of the client.</p>
    </div>

    <svg class="rules" style="top:386px;height:36px" viewBox="0 0 472 36" aria-hidden="true">
      <g stroke="var(--line)" stroke-width="1"><line x1="30" y1="8" x2="440" y2="8"/><line x1="30" y1="28" x2="440" y2="28"/></g>
    </svg>
    <div class="section-tag" style="left:95px;top:384px;width:277px;height:38px">
      <h2 class="section-tag__inner" style="font-size:20px">WHY WORK WITH A CLNC:</h2>
    </div>

    <div class="benefit" style="top:445px">
      <div class="benefit__dot"></div>
      <div class="benefit__box">
        <h3 class="benefit__title">Save Time</h3>
        <p class="benefit__body">By allowing the attorney to focus on legal matters.</p>
      </div>
    </div>
    <div class="benefit" style="top:578px">
      <div class="benefit__dot"></div>
      <div class="benefit__box">
        <h3 class="benefit__title">Save Money</h3>
        <p class="benefit__body benefit__body--small">More cost effective for CLNC to<br>manage medical issues versus MD or<br>attorney completing the review along<br>with early identification of critical<br>issues.</p>
      </div>
    </div>
    <div class="benefit" style="top:712px">
      <div class="benefit__dot"></div>
      <div class="benefit__box">
        <h3 class="benefit__title">Bring healthcare expertise</h3>
        <p class="benefit__body benefit__body--small" style="margin-top:6px">By working with a CLNC well-versed in<br>the inner workings of the healthcare<br>system.</p>
      </div>
    </div>

    <address class="contact contact--web">www.halvorsen-partners.com<br>claire@halvorsen-partners.com<br>(612) 555-0187</address>
    <address class="contact contact--post"><span class="contact__name">R. Halvorsen &amp; Associates LLC</span><br>2190 Larkspur Lane<br>Cedar Ridge, MN 55310</address>
    <div class="card__band card__band--bottom"></div>
  </section>

</div>
</body>
</html>
```